PRICE LIST

I wont a design similar to my business card but not black i wont it very easy to read and simple here is my price list so far

Industry/Entity Type

Business

Font styles to use
Script

```html
<!DOCTYPE html>
<html lang="en">
<head>
<meta charset="utf-8">
<title>Simple Glow – Price List</title>
<link href="https://fonts.googleapis.com/css2?family=Josefin+Sans:wght@300;400;600;700&family=Lobster&display=swap" rel="stylesheet">
<style>
  :root {
    --ink: #231f20;
    --gold: #c9962f;
    --paper: #f4f4f4;
    --white: #ffffff;
    --rule: #3a3a3a;
  }
  * { box-sizing: border-box; margin: 0; padding: 0; }
  html, body { width: 1200px; height: 1000px; overflow: hidden; background: var(--white); }
  body { font-family: "Josefin Sans", sans-serif; color: var(--ink); }

  .price-list {
    position: absolute; left: 281px; top: 37px;
    width: 646px; height: 916px;
    background: var(--paper);
    overflow: hidden;
  }
  .backdrop {
    position: absolute; left: 0; top: 181px; width: 646px; height: 628px;
    background: radial-gradient(ellipse at 70% 45%, #e6e4e2 0%, #efeeed 45%, #f5f5f5 80%);
  }
  .top-band { position: absolute; left: 0; top: 0; width: 100%; height: 14px; background: var(--ink); }
  .header { position: absolute; left: 0; top: 14px; width: 100%; height: 166px; background: #fafafa; border-bottom: 2px solid var(--rule); }

  .brand { position: absolute; left: 80px; top: 60px; font-size: 66px; font-weight: 700; letter-spacing: -1px; line-height: 1; }
  .brand-dot { position: absolute; left: 460px; top: 31px; width: 110px; height: 110px; border-radius: 50%; background: var(--gold); }
  .ornament { position: absolute; left: 124px; top: 124px; width: 276px; height: 36px;
    background: linear-gradient(90deg, rgba(201,150,47,0) 0%, rgba(201,150,47,.85) 25%, rgba(201,150,47,.85) 75%, rgba(201,150,47,0) 100%);
    border-radius: 18px; }

  .supplier { position: absolute; left: 0; top: 214px; width: 100%; text-align: center; }
  .supplier-name { font-size: 26px; font-weight: 600; letter-spacing: .5px; line-height: 1; }
  .supplier-tag { font-size: 10px; font-weight: 400; margin-top: 8px; }

  .column { position: absolute; top: 274px; }
  .column.nails { left: 40px; width: 254px; }
  .column.waxing { left: 374px; width: 232px; }
  .column h2 { font-size: 24px; font-weight: 400; letter-spacing: .3px; margin-bottom: 34px; }

  .service { position: relative; margin-bottom: 16px; }
  .service .name { font-size: 14px; font-weight: 300; line-height: 16px; }
  .service .price { position: absolute; right: 0; top: 0; font-size: 13px; font-weight: 600; }
  .service .detail { font-size: 10px; font-weight: 600; line-height: 13px; }
  .waxing .service { margin-bottom: 18px; }

  .tan-brand { position: absolute; left: 0; top: 666px; width: 100%; display: flex; justify-content: center; align-items: center; gap: 8px; }
  .tan-brand span { font-size: 30px; font-weight: 700; color: var(--ink); }
  .tan-brand::before { content: ""; width: 30px; height: 30px; border-radius: 50%; background: var(--gold); }

  .promo { position: absolute; left: 0; top: 749px; width: 100%; text-align: center; font-size: 16.5px; font-weight: 400; color: var(--ink); }
  .promo strong { font-weight: 600; }

  .social { position: absolute; left: 0; top: 809px; width: 100%; height: 61px; background: #fafafa; border-top: 2px solid var(--rule); }
  .social-item { position: absolute; top: 8px; display: flex; align-items: center; gap: 12px; font-family: "Lobster", cursive; font-size: 26px; }
  .social-item::before { content: ""; width: 42px; height: 42px; border-radius: 50%; background: var(--ink); }
  .social-item.page { left: 14px; }
  .social-item.handle { left: 350px; }

  .contact-band { position: absolute; left: 0; bottom: 0; width: 100%; height: 46px; background: var(--ink); color: var(--white);
    font-size: 16px; font-weight: 600; letter-spacing: .5px; line-height: 19px; padding: 5px 13px 0; display: flex; justify-content: space-between; }
  .contact-band .right { text-align: right; }
</style>
</head>
<body>
<main class="price-list">
  <div class="backdrop" role="img" aria-label="Soft faded photo of a woman with beaded jewellery behind the price list"></div>
  <div class="top-band"></div>

  <header class="header">
    <div class="brand">Simple Glow</div>
    <div class="brand-dot"></div>
    <div class="ornament" role="img" aria-label="Gold decorative flourish under the salon name"></div>
  </header>

  <div class="supplier">
    <div class="supplier-name">Lumina</div>
    <div class="supplier-tag">Professional nail care range</div>
  </div>

  <section class="column nails">
    <h2>Manicures &amp; Pedicures</h2>
    <div class="service"><div class="name">GelGlo Manicure</div><div class="price">$30</div><div class="detail">Cut, shape, cuticles &amp; GelGlo</div></div>
    <div class="service"><div class="name">Deluxe Manicure</div><div class="price">$40</div><div class="detail">Soak, exfoliate, cut, shape, cuticles<br>- polish or add GelGlo for $10</div></div>
    <div class="service"><div class="name">Paraffin Manicure</div><div class="price">$45</div><div class="detail">Soak, exfoliate, paraffin treatment,<br>cut, shape, cuticles<br>- polish or add GelGlo for $5</div></div>
    <div class="service"><div class="name">GelGlo Pedicure</div><div class="price">$30</div><div class="detail">Cut, shape, cuticles &amp; GelGlo</div></div>
    <div class="service"><div class="name">Deluxe Pedicure</div><div class="price">$40</div><div class="detail">Soak, exfoliate, cut, shape, cuticles<br>- polish or add GelGlo for $10</div></div>
    <div class="service"><div class="name">Paraffin Pedicure</div><div class="price">$45</div><div class="detail">Soak, exfoliate, paraffin treatment,<br>cut, shape, cuticles<br>- polish or add GelGlo for $5</div></div>
  </section>

  <section class="column waxing">
    <h2>Waxing &amp; Tinting</h2>
    <div class="service"><div class="name">Eyebrow Wax</div><div class="price">$10</div></div>
    <div class="service"><div class="name">Eyebrow Tint</div><div class="price">$10</div></div>
    <div class="service"><div class="name">Eyelash Tint</div><div class="price">$10</div></div>
    <div class="service"><div class="name">Lip Wax</div><div class="price">$10</div></div>
    <div class="service"><div class="name">Chin Wax</div><div class="price">$10</div></div>
    <div class="service"><div class="name">Underarm</div><div class="price">$15</div></div>
  </section>

  <div class="tan-brand"><span>SunVeil</span></div>
  <p class="promo">The very popular “2 Hour SUNVEIL TAN “in all ranges is now available <strong>for $25.00!</strong></p>

  <div class="social">
    <div class="social-item page">Simple Glow Sun Coast</div>
    <div class="social-item handle">simpleglowsuncoast</div>
  </div>

  <footer class="contact-band">
    <div class="left">Marlee<br>Ph:0400 123 987</div>
    <div class="right">Palm Shores , Sun Coast<br>Flexible Hours 7 Days a week</div>
  </footer>
</main>
</body>
</html>
```